Grivo like IOS/Android app for Okinawa Island - TavuScout

TavuScout is the name of the app
The closest thing that I can relate this app to is a region specific Grivo app. The app is for the island of Okinawa and is geared towards English speaking travelers. The style of app that I prefer is a look and feel similar to that of the new Lodgemere app, color should also be similar if not the same as the lodgemere app.

The app needs to have the following screens

LOGIN SCREEN
1. App login page with a login for chatterly button or create an account option. Personally I would like an image in the background with a real beachy feel, but don't do this if it messes with your design.

2. Depending on the choice of login there will need to be a second login screen to create the account. Lodgemere does this nicely.

PRIMARY HOME
primary page similar to the primary layout when you get into the lodgemere app.
This page is kind of like the home page of the app and should include the following items:
search field
upcoming events
popular things to do
featured restaurants
Featured Places to stay
area guides
Moving here
(this will allow the person to select, housing agencies, auto dealers, schools etc) These are essentially just quick searches.
Each selection should be listed so that the user can swipe to the left or right in order to view more listings under the categories listed above. It will not be the full list but rather a sample.

SIDEBAR POPOUT MENU
Popout sidebar that contains the following selections
Places to Eat
Things to do
Attractions
Beaches
Shop
Farmers Markets
Places to Stay
Schools & DayCare
Housing
Auto
Events
Account settings
Add a business

LIST VIEW
4. List view page for whatever category the user selected. This will show all the listings for the specific category: The top should also have the featured listings for that category

INDIVIDUAL LISTING
5. Listing page
This will include photos, description, hours, map(this can be a button to view the map or the map), Reviews with a leave a review option

AREA GUIDES
6. Area Guides. This is where the user will be able to select a specific area and learn about it. It should include an area where there can be a description, photos with a hero photo image, a map, popular local attractions or things to do, best restaurants in the area, places to stay etc.

PROFILE PAGE
7. Profile page for the user where they can make any updates they need to

Every page but the listing page should include the search bar. When the user clicks in it they should be able to see a drop down of quick select searches or run a regular search.

Logo
I have attached a logo that was made that needs a redesign. The map marker contains the logo for Okinawa within it so it does need to be similar.

If you have any questions or need clarification please send me a message. I will respond promptly.
Thank you,

```html
<!DOCTYPE html>
<html lang="en">
<head>
<meta charset="utf-8">
<title>TavuScout — App Screens</title>
<link href="https://fonts.googleapis.com/css2?family=Lato:wght@300;400;700&display=swap" rel="stylesheet">
<style>
:root{
  --canvas:#1f1f1f;
  --coral:#e5606b;
  --coral-deep:#d9535e;
  --login-red:#de4b3f;
  --chatterly-blue:#3b5ef0;
  --globiq-red:#dd4b3e;
  --white:#ffffff;
  --ink:#333333;
  --muted:#666666;
  --list-bg:#ececec;
  --open:#f0823c;
}
*{box-sizing:border-box;margin:0;padding:0}
html,body{width:1200px;height:1200px;overflow:hidden;background:var(--canvas);font-family:'Lato',sans-serif}
.screen{position:absolute;width:220px;height:389px;overflow:hidden;color:var(--white)}
.screen--coral{background:var(--coral)}
.screen--white{background:var(--white);color:var(--ink)}
.screen--home{background:var(--list-bg);color:var(--ink)}
.photo-bg{position:absolute;inset:0;background:linear-gradient(180deg,#4a2a5c 0%,#8a2f4a 18%,#d9452a 36%,#f08a1e 44%,#b8231c 55%,#4a0d0d 75%,#1a0505 100%)}
.status{position:absolute;top:0;left:0;right:0;height:12px;display:flex;justify-content:space-between;align-items:center;padding:0 5px;font-size:6.5px;font-weight:700;color:var(--white);z-index:3}
.status .time{position:absolute;left:50%;transform:translateX(-50%)}
.battery{display:inline-block;width:12px;height:5px;border:1px solid var(--white);margin-left:4px;vertical-align:middle;position:relative}
.battery::before{content:"";position:absolute;left:0;top:0;bottom:0;width:4px;background:var(--white)}
.layer{position:absolute;left:0;right:0;text-align:center}
.brand-splash{top:186px;display:flex;justify-content:center;align-items:center;gap:6px;font-size:20px;font-weight:400}
.brand-dot{width:18px;height:18px;border-radius:50%;background:var(--white)}
.intro-title{top:56px;font-size:20px;font-weight:400}
.intro-text{top:78px;font-size:15px;font-weight:300;line-height:19px;padding:0 8px}
.btn{position:absolute;left:14px;width:192px;height:25px;display:flex;align-items:center;font-size:10px;color:var(--white)}
.btn .mark{width:13px;height:13px;background:var(--white);margin:0 0 0 10px;opacity:.95}
.btn span{flex:1;text-align:center;padding-right:23px}
.btn--chatterly{top:304px;background:var(--chatterly-blue)}
.btn--globiq{top:334px;background:var(--globiq-red)}
.small-link{font-size:8.5px;color:#f07a55}
.small-link b{color:var(--white);font-weight:400}
.field{position:absolute;left:14px;width:192px;text-align:center;font-size:8px;border-bottom:1px solid rgba(255,255,255,.9);padding-bottom:3px}
.login-btn{position:absolute;left:14px;top:243px;width:192px;height:25px;background:var(--login-red);font-size:10px;display:flex;align-items:center;justify-content:center}
.back{position:absolute;left:14px;top:28px;width:14px;height:12px}
.step-title{top:89px;font-size:16px;font-weight:700}
.step-note{top:120px;font-size:8px;line-height:10.5px;padding:0 24px}
.eye{position:absolute;right:3px;bottom:3px;width:11px;height:7px}
.next{position:absolute;left:178px;top:344px;width:30px;height:30px;border-radius:50%;background:rgba(255,255,255,.3);display:flex;align-items:center;justify-content:center}
.illus{position:absolute;left:50px;top:68px;width:120px;height:120px;border-radius:50%;border:2px solid #e6e6e6;background:radial-gradient(circle at 50% 45%,#f7d948 0 42%,#f4f4f4 43%)}
.dots{top:324px;display:flex;justify-content:center;gap:4px}
.dots i{width:5px;height:5px;border-radius:50%;background:#d5d5d5}
.dots i:first-child{background:var(--coral)}
.appbar{position:absolute;top:0;left:0;right:0;height:37px;background:var(--coral);color:var(--white)}
.appbar .title{position:absolute;top:20px;width:100%;text-align:center;font-size:10.5px}
.appbar svg{position:absolute;top:21px}
.searchbar{position:absolute;top:37px;left:0;right:0;height:25px;background:var(--coral-deep);color:var(--white);font-size:8px;display:flex;align-items:center;padding:0 8px;gap:5px}
.searchbar .done{margin-left:auto}
.menu{position:absolute;left:6px;right:6px;list-style:none}
.menu li{height:24px;background:var(--white);margin-bottom:2.8px;display:flex;align-items:center;font-size:10px;color:#222;position:relative}
.menu li svg.icon{width:16px;height:16px;margin:0 11px 0 8px}
.menu li svg.chev{position:absolute;right:10px;width:6px;height:10px}
.section-label{position:absolute;left:7px;font-size:8.5px;color:#444}
.section-label em{font-style:normal;color:var(--coral)}
.card{position:absolute;left:0;right:0;height:76px}
.card .pic{position:absolute;inset:0}
.pic--salad{background:linear-gradient(135deg,#e8e4dc 0%,#c9b79a 40%,#d84a2e 60%,#86b35a 80%,#e9e9e6 100%)}
.pic--pizza{background:linear-gradient(135deg,#c8822e 0%,#e0a54a 35%,#b2301e 55%,#2a2520 70%,#d9c3a0 100%)}
.card .band{position:absolute;left:0;right:0;bottom:0;height:26px;background:rgba(40,40,50,.75);color:var(--white);padding:3px 7px}
.band .name{font-size:9.5px}
.band .loc{font-size:5.5px;margin-top:1px}
.band .hours{position:absolute;right:18px;top:3px;text-align:right;font-size:5.5px}
.band .hours b{display:block;color:var(--open);font-size:8.5px;font-weight:400}
</style>
</head>
<body>

<!-- Row 1 -->
<section class="screen" style="left:150px;top:8px">
  <div class="photo-bg" role="img" aria-label="Sunset over the sea, sun low on the horizon with red light on the water"></div>
  <div class="status"><span>●●○○○ Carrio</span><span class="time">14:39</span><span>◎<i class="battery"></i></span></div>
  <div class="layer brand-splash"><i class="brand-dot"></i>TavuScout</div>
</section>

<section class="screen" style="left:374px;top:8px">
  <div class="photo-bg" role="img" aria-label="Sunset over the sea, sun low on the horizon with red light on the water"></div>
  <div class="status"><span>●●○○○ Carrio</span><span class="time">14:39</span><span>◎<i class="battery"></i></span></div>
  <div class="layer intro-title">TavuScout</div>
  <div class="layer intro-text">TavuScout is your local guide to finding just the place to eat, shop, drink, relax, and play</div>
  <div class="btn btn--chatterly"><i class="mark"></i><span>START WITH CHATTERLY</span></div>
  <div class="btn btn--globiq"><i class="mark"></i><span>START WITH GLOBIQ</span></div>
  <div class="layer small-link" style="top:370px">Already have an account? <b>Login</b></div>
</section>

<section class="screen" style="left:600px;top:8px">
  <div class="photo-bg" role="img" aria-label="Sunset over the sea, sun low on the horizon with red light on the water"></div>
  <div class="status"><span>●●○○○ Carrio</span><span class="time">14:39</span><span>◎<i class="battery"></i></span></div>
  <div class="layer intro-title">TavuScout</div>
  <div class="layer intro-text">TavuScout is your local guide to finding just the place to eat, shop, drink, relax, and play</div>
  <div class="field" style="top:182px">Email</div>
  <div class="field" style="top:210px">Password</div>
  <div class="login-btn">LOGIN</div>
  <div class="layer" style="top:284px;font-size:8.5px">Forgot Password?</div>
  <div class="layer" style="top:323px;font-size:8.5px">Don't have an account? <b>Signup</b></div>
</section>

<section class="screen screen--coral" style="left:826px;top:8px">
  <div class="status"><span>●●○○○ Carrio</span><span class="time">14:39</span><span>◎<i class="battery"></i></span></div>
  <svg class="back" viewBox="0 0 14 12"><path d="M13 6H1M6 1L1 6l5 5" fill="none" stroke="#fff" stroke-width="1.3"/></svg>
  <div class="layer step-title">What's your name?</div>
  <div class="field" style="top:153px">First name</div>
  <div class="field" style="top:193px">Last name</div>
  <div class="next"><svg width="8" height="14" viewBox="0 0 8 14"><path d="M1 1l6 6-6 6" fill="none" stroke="#fff" stroke-width="1.4"/></svg></div>
</section>

<!-- Row 2 -->
<section class="screen screen--coral" style="left:150px;top:406px">
  <div class="status"><span>●●○○○ Carrio</span><span class="time">14:39</span><span>◎<i class="battery"></i></span></div>
  <svg class="back" viewBox="0 0 14 12"><path d="M13 6H1M6 1L1 6l5 5" fill="none" stroke="#fff" stroke-width="1.3"/></svg>
  <div class="layer step-title">Your email?</div>
  <div class="field" style="top:153px">Email Address</div>
  <div class="next"><svg width="8" height="14" viewBox="0 0 8 14"><path d="M1 1l6 6-6 6" fill="none" stroke="#fff" stroke-width="1.4"/></svg></div>
</section>

<section class="screen screen--coral" style="left:380px;top:406px">
  <div class="status"><span>●●○○○ Carrio</span><span class="time">14:39</span><span>◎<i class="battery"></i></span></div>
  <svg class="back" viewBox="0 0 14 12"><path d="M13 6H1M6 1L1 6l5 5" fill="none" stroke="#fff" stroke-width="1.3"/></svg>
  <div class="layer step-title">Create a password ...</div>
  <div class="layer step-note">Password must be at least 6 charectors and include a combination of uppercase and lowercase letters &amp; numbers</div>
  <div class="field" style="top:174px">Password<svg class="eye" viewBox="0 0 11 7"><ellipse cx="5.5" cy="3.5" rx="5" ry="3" fill="#fff"/><circle cx="5.5" cy="3.5" r="1.4" fill="#e5606b"/></svg></div>
  <div class="next"><svg width="8" height="14" viewBox="0 0 8 14"><path d="M1 1l6 6-6 6" fill="none" stroke="#fff" stroke-width="1.4"/></svg></div>
</section>

<section class="screen screen--coral" style="left:606px;top:406px">
  <div class="status"><span>●●○○○ Carrio</span><span class="time">14:39</span><span>◎<i class="battery"></i></span></div>
  <svg class="back" viewBox="0 0 14 12"><path d="M13 6H1M6 1L1 6l5 5" fill="none" stroke="#fff" stroke-width="1.3"/></svg>
  <div class="layer step-title">When is your Birthday ?</div>
  <div class="layer step-note" style="padding:0 14px">You must be at least 18 year old to use TavuScout. And we will not share anything with anyone.</div>
  <div class="field" style="top:174px">Password<svg class="eye" viewBox="0 0 11 7"><ellipse cx="5.5" cy="3.5" rx="5" ry="3" fill="#fff"/><circle cx="5.5" cy="3.5" r="1.4" fill="#e5606b"/></svg></div>
  <div class="next"><svg width="8" height="14" viewBox="0 0 8 14"><path d="M1 1l6 6-6 6" fill="none" stroke="#fff" stroke-width="1.4"/></svg></div>
</section>

<section class="screen screen--white" style="left:830px;top:406px">
  <div class="illus" role="img" aria-label="Illustration of a hotel building between clouds with staff standing beside it"></div>
  <div class="layer" style="top:200px;font-size:12.5px;color:#444">Near By</div>
  <div class="layer" style="top:224px;font-size:9.5px;line-height:12.5px;color:#555;padding:0 16px">Search for nearby restaurants, shops, and services</div>
  <div class="layer dots"><i></i><i></i><i></i></div>
</section>

<!-- Row 3 -->
<section class="screen screen--home" style="left:374px;top:802px">
  <div class="status"><span>●●○○○ Carrio</span><span class="time">14:39</span><span>◎<i class="battery"></i></span></div>
  <header class="appbar">
    <svg style="left:9px" width="13" height="9" viewBox="0 0 13 9"><path d="M0 1h13M0 4.5h13M0 8h13" stroke="#fff" stroke-width="1"/></svg>
    <div class="title">TavuScout</div>
    <svg style="right:9px" width="9" height="9" viewBox="0 0 9 9"><circle cx="3.8" cy="3.8" r="3" fill="none" stroke="#fff"/><path d="M6 6l2.5 2.5" stroke="#fff"/></svg>
  </header>
  <ul class="menu" style="top:44px">
    <li><svg class="icon" viewBox="0 0 16 16"><rect x="1.5" y="3" width="13" height="11.5" fill="none" stroke="#444"/><path d="M1.5 6h13M5 1.5v3M11 1.5v3" stroke="#444"/></svg>Upcoming events<svg class="chev" viewBox="0 0 6 10"><path d="M1 1l4 4-4 4" fill="none" stroke="#333" stroke-width="1.2"/></svg></li>
    <li><svg class="icon" viewBox="0 0 16 16"><path d="M8 15V8M8 8C6 3 2 3 1 4c1 3 4 4 7 4zM8 8c2-5 6-5 7-4-1 3-4 4-7 4z" fill="none" stroke="#444"/></svg>Popular things to do<svg class="chev" viewBox="0 0 6 10"><path d="M1 1l4 4-4 4" fill="none" stroke="#333" stroke-width="1.2"/></svg></li>
    <li><svg class="icon" viewBox="0 0 16 16"><path d="M4 1v14M2 1v4c0 1 1 2 2 2s2-1 2-2V1M11 15V1c2 1 3 3 3 6h-3" fill="none" stroke="#444"/></svg>Featured restaurants<svg class="chev" viewBox="0 0 6 10"><path d="M1 1l4 4-4 4" fill="none" stroke="#333" stroke-width="1.2"/></svg></li>
    <li><svg class="icon" viewBox="0 0 16 16"><rect x="2" y="4" width="12" height="11" fill="none" stroke="#444"/><path d="M5 2h6v2M4 7h2M7 7h2M10 7h2M4 10h2M7 10h2M10 10h2" stroke="#444"/></svg>Featured Places to stay<svg class="chev" viewBox="0 0 6 10"><path d="M1 1l4 4-4 4" fill="none" stroke="#333" stroke-width="1.2"/></svg></li>
    <li><svg class="icon" viewBox="0 0 16 16"><path d="M8 1v14M5 15h6M2 3h11l2 2-2 2H2z" fill="none" stroke="#444"/></svg>Area guides<svg class="chev" viewBox="0 0 6 10"><path d="M1 1l4 4-4 4" fill="none" stroke="#333" stroke-width="1.2"/></svg></li>
    <li><svg class="icon" viewBox="0 0 16 16"><path d="M8 1v14M1 8h14M6 3l2-2 2 2M6 13l2 2 2-2M3 6L1 8l2 2M13 6l2 2-2 2" fill="none" stroke="#444"/></svg>Moving here<svg class="chev" viewBox="0 0 6 10"><path d="M1 1l4 4-4 4" fill="none" stroke="#333" stroke-width="1.2"/></svg></li>
  </ul>
  <div class="section-label" style="top:214px">Popular <em>restaurant</em> near by location</div>
  <article class="card" style="top:228px"><div class="pic pic--salad" role="img" aria-label="Photo of a plated dish with salad and tomatoes"></div><div class="band"><div class="name">Capricia</div><div class="loc">⚲ wolmington, Naha</div><div class="hours"><b>Open</b>11 AM - 9 PM</div></div></article>
  <article class="card" style="top:304px"><div class="pic pic--pizza" role="img" aria-label="Photo of a pizza with pepperoni and olives"></div><div class="band"><div class="name">Greig Cafe &amp; Restaurant</div><div class="loc">⚲ wolmington, Naha</div><div class="hours"><b>Open</b>10AM - 11 PM</div></div></article>
</section>

<section class="screen screen--home" style="left:620px;top:802px">
  <div class="status"><span>●●○○○ Carrio</span><span class="time">14:39</span><span>◎<i class="battery"></i></span></div>
  <header class="appbar">
    <svg style="left:9px" width="13" height="9" viewBox="0 0 13 9"><path d="M0 1h13M0 4.5h13M0 8h13" stroke="#fff" stroke-width="1"/></svg>
    <div class="title">TavuScout</div>
    <svg style="right:9px;top:19px" width="9" height="11" viewBox="0 0 9 11"><path d="M4.5 11V1M1 4.5l3.5-3.5 3.5 3.5" fill="none" stroke="#fff"/></svg>
  </header>
  <div class="searchbar"><svg width="9" height="9" viewBox="0 0 9 9"><circle cx="3.8" cy="3.8" r="3" fill="none" stroke="#fff"/><path d="M6 6l2.5 2.5" stroke="#fff"/></svg>Search here<span class="done">Done</span></div>
  <ul class="menu" style="top:74px">
    <li><svg class="icon" viewBox="0 0 16 16"><rect x="1.5" y="3" width="13" height="11.5" fill="none" stroke="#444"/><path d="M1.5 6h13M5 1.5v3M11 1.5v3" stroke="#444"/></svg>Upcoming events<svg class="chev" viewBox="0 0 6 10"><path d="M1 1l4 4-4 4" fill="none" stroke="#333" stroke-width="1.2"/></svg></li>
    <li><svg class="icon" viewBox="0 0 16 16"><path d="M8 15V8M8 8C6 3 2 3 1 4c1 3 4 4 7 4zM8 8c2-5 6-5 7-4-1 3-4 4-7 4z" fill="none" stroke="#444"/></svg>Popular things to do<svg class="chev" viewBox="0 0 6 10"><path d="M1 1l4 4-4 4" fill="none" stroke="#333" stroke-width="1.2"/></svg></li>
    <li><svg class="icon" viewBox="0 0 16 16"><path d="M4 1v14M2 1v4c0 1 1 2 2 2s2-1 2-2V1M11 15V1c2 1 3 3 3 6h-3" fill="none" stroke="#444"/></svg>Featured restaurants<svg class="chev" viewBox="0 0 6 10"><path d="M1 1l4 4-4 4" fill="none" stroke="#333" stroke-width="1.2"/></svg></li>
    <li><svg class="icon" viewBox="0 0 16 16"><rect x="2" y="4" width="12" height="11" fill="none" stroke="#444"/><path d="M5 2h6v2M4 7h2M7 7h2M10 7h2M4 10h2M7 10h2M10 10h2" stroke="#444"/></svg>Featured Places to stay<svg class="chev" viewBox="0 0 6 10"><path d="M1 1l4 4-4 4" fill="none" stroke="#333" stroke-width="1.2"/></svg></li>
    <li><svg class="icon" viewBox="0 0 16 16"><path d="M8 1v14M5 15h6M2 3h11l2 2-2 2H2z" fill="none" stroke="#444"/></svg>Area guides<svg class="chev" viewBox="0 0 6 10"><path d="M1 1l4 4-4 4" fill="none" stroke="#333" stroke-width="1.2"/></svg></li>
    <li><svg class="icon" viewBox="0 0 16 16"><path d="M8 1v14M1 8h14M6 3l2-2 2 2M6 13l2 2 2-2M3 6L1 8l2 2M13 6l2 2-2 2" fill="none" stroke="#444"/></svg>Moving here<svg class="chev" viewBox="0 0 6 10"><path d="M1 1l4 4-4 4" fill="none" stroke="#333" stroke-width="1.2"/></svg></li>
  </ul>
  <div class="section-label" style="top:244px">Popular <em>restaurant</em> near by location</div>
  <article class="card" style="top:258px"><div class="pic pic--salad" role="img" aria-label="Photo of a plated dish with salad and tomatoes"></div><div class="band"><div class="name">Capricia</div><div class="loc">⚲ wolmington, Naha</div><div class="hours"><b>Open</b>11 AM - 9 PM</div></div></article>
  <article class="card" style="top:334px"><div class="pic pic--pizza" role="img" aria-label="Photo of a pizza with pepperoni and olives"></div><div class="band"><div class="name">Greig Cafe &amp; Restaurant</div><div class="loc">⚲ wolmington, Naha</div><div class="hours"><b>Open</b>10AM - 11 PM</div></div></article>
</section>

</body>
</html>
```